quiet orchard

It is a small business that is looking to sell medical supplies and services. later down the line it will branch off to help solve other world problems, i.e. global warming and raw material shortages.
but we will start with hospital equipment and supplies.

Target Market(s)

all medical facilities

Coding

Coded - Design and coding required

Number of Pages Required

1 page

```html
<!DOCTYPE html>
<html lang="en">
<head>
<meta charset="utf-8">
<title>Quiet Orchard – Medical Supplies</title>
<link href="https://fonts.googleapis.com/css2?family=Montserrat:wght@600;700;800&family=Roboto:wght@400;500;700&display=swap" rel="stylesheet">
<style>
:root{
  --green:#0b4d47;
  --green-dark:#073f3a;
  --ink:#222;
  --text:#6b6b6b;
  --light:#f4f4f4;
  --footer:#262626;
  --footer-text:#e6e6e6;
  --footer-icon:#2f5f59;
  --white:#fff;
}
*{margin:0;padding:0;box-sizing:border-box}
html,body{width:1200px;height:3787px;overflow:hidden}
body{position:relative;background:var(--white);font-family:'Roboto',sans-serif;color:var(--ink)}
.abs{position:absolute}
.heading{font-family:'Montserrat',sans-serif;font-weight:700;text-transform:uppercase;letter-spacing:.5px}
.heading .accent{color:var(--green)}
.btn{position:absolute;display:flex;align-items:center;justify-content:center;background:var(--green);color:var(--white);font-weight:700;font-size:15px;text-transform:uppercase;border-radius:4px;text-decoration:none}
.para{font-size:14px;line-height:26px;color:var(--text)}
.photo{position:absolute}

/* header */
.site-header{left:0;top:0;width:1200px;height:85px}
.brand{left:110px;top:26px;font-family:'Montserrat',sans-serif;font-weight:700;font-size:25px;color:var(--ink);white-space:nowrap}
.brand .accent{color:var(--green)}
.nav{left:375px;top:34px;display:flex;gap:22px;font-size:13.5px;font-weight:500;color:var(--ink);white-space:nowrap}
.nav .active{color:var(--green);position:relative}
.nav .active::before{content:"";position:absolute;left:0;right:0;top:-34px;height:3px;background:var(--green)}
.call-box{left:953px;top:0;width:247px;height:85px;background:var(--green);color:var(--white);text-align:center;padding-top:17px}
.call-box .label{font-size:14px;font-weight:700}
.call-box .number{font-size:19px;font-weight:700;margin-top:6px}

/* hero */
.hero{left:0;top:85px;width:1200px;height:600px;background:linear-gradient(110deg,#cfdbee 0%,#6b8fcc 35%,#a9c1e4 60%,#1d4ea5 100%)}
.hero-title{left:0;width:1200px;top:287px;text-align:center;font-family:'Montserrat',sans-serif;font-weight:800;font-size:38px;color:#1c1c1c}
.hero-title .accent{color:var(--green)}
.hero-sub{left:300px;width:600px;top:345px;text-align:center;font-size:18px;font-weight:500;line-height:29px;color:#1c1c1c}
.hero-arrow{top:367px}

/* about */
.about-title{left:0;width:1200px;top:775px;text-align:center;font-size:38px}
.about-text{left:135px;width:930px;top:843px;text-align:center}

/* supplies */
.supplies{left:0;top:1098px;width:1200px;height:662px;background:linear-gradient(180deg,#1c5d56,#0f4e48);border-radius:4px}
.supplies-title{left:0;width:1200px;top:1172px;text-align:center;font-size:35px;color:var(--white)}
.card{position:absolute;top:1250px;width:230px;height:325px;background:var(--white);border-radius:6px;padding:5px}
.card .photo{position:relative;width:220px;height:264px}
.card-name{text-align:center;font-size:15px;font-weight:500;color:var(--ink);margin-top:21px}
.btn-light{background:var(--white);color:var(--green)}

/* features */
.frame{position:absolute;background:var(--green);border-radius:10px}
.feature-title{font-size:31px;color:#1c1c1c}
.feature-text{text-align:justify}

/* blog */
.blog{left:0;top:2948px;width:1200px;height:526px;background:var(--light)}
.blog-title{left:0;width:1200px;top:3007px;text-align:center;font-size:38px;color:#1c1c1c}
.post{position:absolute;top:3087px;width:310px;height:319px;background:var(--white);border:1px solid #ddd;box-shadow:0 0 6px rgba(0,0,0,.08);padding:8px;text-align:center}
.post .photo{position:relative;width:294px;height:189px}
.post-date{margin-top:20px;font-size:13px;color:#555;display:flex;align-items:center;justify-content:center;gap:8px}
.post-title{margin-top:18px;font-size:15px;font-weight:700;line-height:25px;text-transform:uppercase;color:#222}
.post-title.featured{color:var(--green)}

/* footer */
.site-footer{left:0;top:3474px;width:1200px;height:313px;background:var(--footer)}
.foot-brand{left:110px;top:3565px;font-family:'Montserrat',sans-serif;font-weight:700;font-size:25px;color:var(--white);white-space:nowrap}
.social{top:3621px;width:34px;height:34px;border-radius:50%;background:var(--white);display:flex;align-items:center;justify-content:center}
.social::after{content:"";width:12px;height:12px;border-radius:50%;background:var(--green)}
.foot-col{color:var(--footer-text)}
.foot-col h4{font-size:17px;font-weight:700;color:var(--white);margin-bottom:20px;text-transform:uppercase}
.foot-col ul{list-style:none}
.foot-col li{font-size:15px;line-height:18px;height:29.4px;display:flex;align-items:flex-start;gap:18px;color:var(--footer-text)}
.foot-col li svg{flex:none;margin-top:3px}
.foot-rule{left:110px;top:3729px;width:978px;height:1px;background:#555}
.copyright{left:0;width:1200px;top:3745px;text-align:center;font-size:12px;color:var(--white)}
</style>
</head>
<body>

<header class="abs site-header">
  <div class="abs brand">QUIET <span class="accent">ORCHARD</span></div>
  <nav class="abs nav">
    <span class="active">HOME</span><span>ABOUT</span><span>OUR MEDICAL SUPPLIES</span><span>SERVICES</span><span>BLOG</span><span>CONTACT</span>
  </nav>
  <div class="abs call-box"><div class="label">CALL US:</div><div class="number">+1 (555) 014 2020</div></div>
</header>

<section>
  <div class="abs hero" role="img" aria-label="Scientist in a lab coat and safety goggles holding a test tube in a laboratory"></div>
  <svg class="abs hero-arrow" style="left:40px" width="24" height="36" viewBox="0 0 24 36"><path d="M18 4 L5 18 L18 32" fill="none" stroke="#fff" stroke-width="4"/></svg>
  <svg class="abs hero-arrow" style="left:1136px" width="24" height="36" viewBox="0 0 24 36"><path d="M6 4 L19 18 L6 32" fill="none" stroke="#fff" stroke-width="4"/></svg>
  <h1 class="abs hero-title">WELCOME TO <span class="accent">QUIET ORCHARD</span></h1>
  <p class="abs hero-sub">At vero eos et accusamus et iusto odio dignissimos duci<br>mus qui blanditiis praesentium.</p>
  <a class="btn" style="left:522px;top:426px;width:156px;height:50px">Get Started</a>
</section>

<section>
  <h2 class="abs heading about-title"><span class="accent">About</span> Quiet Orchard</h2>
  <p class="abs para about-text">At vero eos et accusamus et iusto odio dignissimos ducimus qui blanditiis praesentium voluptatum deleniti atque corrupti quos dolores et quas molestias excepturi sint occaecati cupiditate non provident, similique sunt in culpa qui officia deserunt mollitia animi, id est laborum et dolorum fuga. Et harum quidem rerum facilis est et expedita distinctio.</p>
  <a class="btn" style="left:522px;top:953px;width:156px;height:51px">Learn More</a>
</section>

<section>
  <div class="abs supplies" role="img" aria-label="Faint hospital interior behind a dark green overlay"></div>
  <h2 class="abs heading supplies-title">Our Medical Supplies</h2>
  <div class="card" style="left:112px"><div class="photo" role="img" aria-label="Ventilator machine" style="background:linear-gradient(160deg,#e9eef2,#b9c9d3)"></div><div class="card-name">VENTILATOR</div></div>
  <div class="card" style="left:361px"><div class="photo" role="img" aria-label="EKG machine with screen" style="background:linear-gradient(160deg,#dcdfe2,#8b9298)"></div><div class="card-name">EKG MACHINES</div></div>
  <div class="card" style="left:610px"><div class="photo" role="img" aria-label="X-ray machine in an operating room" style="background:linear-gradient(160deg,#eef1f3,#9ba9b1)"></div><div class="card-name">X-RAY MACHINE</div></div>
  <div class="card" style="left:859px"><div class="photo" role="img" aria-label="Hand holding a tablet showing patient vitals" style="background:linear-gradient(160deg,#c8d4e4,#3d4c66)"></div><div class="card-name">PATIENT MONITOR</div></div>
  <a class="btn btn-light" style="left:509px;top:1629px;width:182px;height:50px">View All Supplies</a>
</section>

<section>
  <div class="frame" style="left:112px;top:1859px;width:256px;height:445px"></div>
  <div class="photo" role="img" aria-label="Hand holding a glass globe with a green plant, surrounded by eco icons" style="left:159px;top:1910px;width:441px;height:343px;border-radius:10px;background:radial-gradient(circle at 55% 45%,#d9e77a,#5f8f2a 45%,#2d5a1c)"></div>
  <h2 class="abs heading feature-title" style="left:662px;top:1924px">Global <span class="accent">Warming</span></h2>
  <p class="abs para feature-text" style="left:662px;top:1989px;width:426px">At vero eos et accusamus et iusto odio dignissimos ducimus qui blanditiis praesentium voluptatum deleniti atque corrupti quos dolores et quas molestias excepturi sint occaecati cupiditate non provident, similique sunt in culpa qui officia deserunt mollitia animi, id est laborum et dolorum fuga. Et harum quidem rerum facilis est et expedita distinctio.</p>
  <a class="btn" style="left:662px;top:2182px;width:138px;height:50px">Read More</a>

  <div class="frame" style="left:831px;top:2404px;width:257px;height:445px"></div>
  <div class="photo" role="img" aria-label="Technician at computer screens watching a patient in an MRI scanner" style="left:599px;top:2456px;width:442px;height:341px;border-radius:10px;background:linear-gradient(120deg,#e4e9ef,#97a9c0 50%,#1f3e7a)"></div>
  <h2 class="abs heading feature-title" style="left:112px;top:2468px"><span class="accent">Raw</span> Material</h2>
  <p class="abs para feature-text" style="left:112px;top:2534px;width:426px">At vero eos et accusamus et iusto odio dignissimos ducimus qui blanditiis praesentium voluptatum deleniti atque corrupti quos dolores et quas molestias excepturi sint occaecati cupiditate non provident, similique sunt in culpa qui officia deserunt mollitia animi, id est laborum et dolorum fuga. Et harum quidem rerum facilis est et expedita distinctio.</p>
  <a class="btn" style="left:112px;top:2726px;width:138px;height:51px">Read More</a>
</section>

<section>
  <div class="abs blog"></div>
  <h2 class="abs heading blog-title">Latest <span class="accent">Blog</span></h2>
  <article class="post" style="left:112px"><div class="photo" role="img" aria-label="Doctors with a patient at an MRI scanner" style="background:linear-gradient(150deg,#eef2f5,#a8bccb)"></div>
    <div class="post-date"><svg width="13" height="13" viewBox="0 0 13 13"><rect x="1" y="2" width="11" height="10" fill="none" stroke="#666" stroke-width="1.4"/><path d="M1 5h11M4 0v3M9 0v3" stroke="#666" stroke-width="1.4"/></svg>17 JAN 2022</div>
    <div class="post-title">Lorem ipsum dolor sit amet<br>consectetur adip</div></article>
  <article class="post" style="left:444px"><div class="photo" role="img" aria-label="Intensive care monitors beside a hospital bed" style="background:linear-gradient(150deg,#3a5fb0,#c9d4e8 60%,#2b4a8c)"></div>
    <div class="post-date"><svg width="13" height="13" viewBox="0 0 13 13"><rect x="1" y="2" width="11" height="10" fill="none" stroke="#666" stroke-width="1.4"/><path d="M1 5h11M4 0v3M9 0v3" stroke="#666" stroke-width="1.4"/></svg>17 JAN 2022</div>
    <div class="post-title featured">Lorem ipsum dolor sit amet<br>consectetur adip</div></article>
  <article class="post" style="left:778px"><div class="photo" role="img" aria-label="Lab researcher at a microscope" style="background:linear-gradient(150deg,#f1f3f4,#b8c5cc)"></div>
    <div class="post-date"><svg width="13" height="13" viewBox="0 0 13 13"><rect x="1" y="2" width="11" height="10" fill="none" stroke="#666" stroke-width="1.4"/><path d="M1 5h11M4 0v3M9 0v3" stroke="#666" stroke-width="1.4"/></svg>17 JAN 2022</div>
    <div class="post-title">Lorem ipsum dolor sit amet<br>consectetur adip</div></article>
</section>

<footer>
  <div class="abs site-footer"></div>
  <div class="abs foot-brand">QUIET ORCHARD</div>
  <span class="abs social" style="left:149px" aria-label="Social link"></span>
  <span class="abs social" style="left:190px" aria-label="Social link"></span>
  <span class="abs social" style="left:231px" aria-label="Social link"></span>

  <div class="abs foot-col" style="left:387px;top:3521px">
    <h4>Quick Links</h4>
    <ul>
      <li><svg width="12" height="12"><circle cx="6" cy="6" r="5.5" fill="#2f5f59"/><path d="M5 3.5 7.5 6 5 8.5" stroke="#262626" fill="none"/></svg>Home</li>
      <li><svg width="12" height="12"><circle cx="6" cy="6" r="5.5" fill="#2f5f59"/><path d="M5 3.5 7.5 6 5 8.5" stroke="#262626" fill="none"/></svg>About</li>
      <li><svg width="12" height="12"><circle cx="6" cy="6" r="5.5" fill="#2f5f59"/><path d="M5 3.5 7.5 6 5 8.5" stroke="#262626" fill="none"/></svg>Our Medical Supplies</li>
      <li><svg width="12" height="12"><circle cx="6" cy="6" r="5.5" fill="#2f5f59"/><path d="M5 3.5 7.5 6 5 8.5" stroke="#262626" fill="none"/></svg>Services</li>
      <li><svg width="12" height="12"><circle cx="6" cy="6" r="5.5" fill="#2f5f59"/><path d="M5 3.5 7.5 6 5 8.5" stroke="#262626" fill="none"/></svg>Contact</li>
    </ul>
  </div>
  <div class="abs foot-col" style="left:663px;top:3521px">
    <h4>About Links</h4>
    <ul>
      <li><svg width="12" height="12"><circle cx="6" cy="6" r="5.5" fill="#2f5f59"/><path d="M5 3.5 7.5 6 5 8.5" stroke="#262626" fill="none"/></svg>Blog</li>
      <li><svg width="12" height="12"><circle cx="6" cy="6" r="5.5" fill="#2f5f59"/><path d="M5 3.5 7.5 6 5 8.5" stroke="#262626" fill="none"/></svg>Privacy Policy</li>
      <li><svg width="12" height="12"><circle cx="6" cy="6" r="5.5" fill="#2f5f59"/><path d="M5 3.5 7.5 6 5 8.5" stroke="#262626" fill="none"/></svg>Terms Of Use</li>
      <li><svg width="12" height="12"><circle cx="6" cy="6" r="5.5" fill="#2f5f59"/><path d="M5 3.5 7.5 6 5 8.5" stroke="#262626" fill="none"/></svg>Legal Support</li>
    </ul>
  </div>
  <div class="abs foot-col" style="left:897px;top:3521px">
    <h4>Contact</h4>
    <ul>
      <li style="height:61px;line-height:29px;margin-top:-6px"><svg width="12" height="14" viewBox="0 0 12 14" style="margin-top:9px"><path d="M6 13C2 8 1 6.5 1 5a5 5 0 0 1 10 0c0 1.5-1 3-5 8z" fill="#2f5f59"/><circle cx="6" cy="5" r="1.8" fill="#262626"/></svg><span>465, Lorum Ipsum Dol,<br>United States</span></li>
      <li><svg width="13" height="13" viewBox="0 0 13 13"><path d="M2 1l2.5 0 1.2 3-1.6 1.2a7 7 0 0 0 3.7 3.7L9 7.3l3 1.2V11a1 1 0 0 1-1 1A10 10 0 0 1 1 2a1 1 0 0 1 1-1z" fill="#2f5f59"/></svg>+1 (555) 014 2020</li>
      <li><svg width="14" height="11" viewBox="0 0 14 11"><rect x="0" y="0" width="14" height="11" rx="1" fill="#2f5f59"/><path d="M1 1l6 5 6-5" stroke="#262626" fill="none" stroke-width="1.3"/></svg>info@quietorchard.com</li>
    </ul>
  </div>
  <div class="abs foot-rule"></div>
  <div class="abs copyright">© 2022 <b>QUIET ORCHARD</b>. All Rights Reserved</div>
</footer>

</body>
</html>
```